Start-up Dog Daycare Needs a Retractable Banner Design for Career Fair

We are a dog daycare located in San Francisco, California, called TailNest Dog Daycare. Our small but dog-knowledgeable team gets to interact with and care for dogs on a daily basis where we supervise playgroups of various sizes. We will like a modern yet fun banner to attract potential new hires and interns. We will like the final design to communicate that we are seeking people who love dogs but who are also hard workers that can thrive in a team setting.

The product specs are as follows:
Document Trim Size - 33.13 X 86.18 inches (84.1 X 218.9cm) with 3312 X 8618 pixels.
Full Bleed Size - 33.38 X 86.43 inches (84.8 X 219.5cm) with 3338 X 8643 pixels.

Additionally, to get a better idea of our brand, attached will be our Company Brand Identity.
Furthermore, attached will be the text we will like included onto our banner.

Target Market(s)

Students at a University

Industry/Entity Type

Pet Care

Font styles to use
Sans Serif

Colors
33a6d7
fbee3e

Requirements
Must have
• Our company logo must be incorporated onto our banner.
• Please include the text in the following order:
• 1. "Dog lovers come talk to us"
• 2. "Internships and full-time positions available"
• Banner Size Specifications:
• Full Bleed Size
• 33.38" x 86.43"
• 84.8 x 219.5 cm
• 3338 x 8643 pixels
• Document Trim Size
• 33.13" x 86.18"
• 84.1 x 218.9 cm
• 3312 x 8618 pixels
• Finished artwork should extend to fill the full bleed area to avoid white edges around.
Nice to have
• - Colors Blue and Yellow
• - Image(s) of a dog(s) playing

```html
<!DOCTYPE html>
<html lang="en">
<head>
<meta charset="utf-8">
<title>TailNest Dog Daycare – Career Fair Banner</title>
<link rel="stylesheet" href="https://fonts.googleapis.com/css2?family=Baloo+2:wght@600;800&family=Montserrat:wght@700&display=swap">
<style>
  :root {
    --stage: #000000;
    --sky: #87c9e8;
    --sky-deep: #6fb9dc;
    --sun: #f9ee45;
    --sun-shade: #d4c818;
    --brand-blue: #33a6d7;
    --brand-yellow: #fbee3e;
    --ink: #1d1d1b;
    --white: #ffffff;
  }
  * { margin: 0; padding: 0; box-sizing: border-box; }
  html, body {
    width: 1200px; height: 1200px; overflow: hidden;
    background: var(--stage);
  }
  .banner {
    position: absolute;
    left: 368px; top: 0;
    width: 464px; height: 1186px;
    background: var(--sky);
    overflow: hidden;
    font-family: "Baloo 2", sans-serif;
    text-align: center;
  }
  .banner-waves {
    position: absolute; inset: 0;
    width: 464px; height: 1186px;
  }
  .brand {
    position: absolute; left: 0; right: 0; top: 30px;
    display: flex; flex-direction: column; align-items: center;
  }
  .brand-dot {
    width: 58px; height: 58px; border-radius: 50%;
    background: var(--brand-yellow);
    margin-bottom: 18px;
  }
  .brand-name {
    font-family: "Baloo 2", sans-serif;
    font-weight: 800;
    font-size: 30px; line-height: 1;
    color: var(--ink);
  }
  .brand-name span { display: block; font-size: 13px; letter-spacing: 2px; margin-top: 10px; }
  .headline {
    position: absolute; left: 0; right: 0; top: 200px;
    color: var(--white);
    font-weight: 800;
    line-height: 1;
  }
  .headline-main { display: block; font-size: 56px; }
  .headline-sub { display: block; font-size: 36px; margin-top: 4px; }
  .dog-photo {
    position: absolute;
    left: 16px; top: 340px;
    width: 420px; height: 340px;
    border-radius: 40% 40% 8px 8px;
    background: radial-gradient(ellipse at 55% 55%, #2a2c30 0%, #3b4047 45%, rgba(135,201,232,0) 75%);
  }
  .offer {
    position: absolute; left: 0; right: 0; top: 824px;
    color: var(--brand-blue);
    font-weight: 800;
    font-size: 46px;
    line-height: 51px;
  }
  .offer span { display: block; }
</style>
</head>
<body>
  <main class="banner">
    <svg class="banner-waves" viewBox="0 0 464 1186" aria-hidden="true">
      <path d="M232 744 Q 360 700 464 680 L464 822 Q 350 768 232 744 Z" fill="var(--sun-shade)"/>
      <path d="M0 704 Q 260 732 464 822 L464 1186 L0 1186 Z" fill="var(--sun)"/>
    </svg>

    <header class="brand">
      <div class="brand-dot"></div>
      <p class="brand-name">TailNest<span>DOG DAYCARE</span></p>
    </header>

    <h1 class="headline">
      <span class="headline-main">Dog Lovers</span>
      <span class="headline-sub">come talk to us!</span>
    </h1>

    <div class="dog-photo" role="img" aria-label="Photo of a black and white border collie peeking over a ledge with its paws resting on the edge"></div>

    <p class="offer">
      <span>Internships</span>
      <span>and full-time</span>
      <span>positions</span>
      <span>available</span>
    </p>
  </main>
</body>
</html>
```